Redesign logo + Business card for Car tuning/diagnostics

Hi, after a LOGO AND BUSINESS CARD. I need a double-sided business card to be designed. And information added to it as below. I have added some pictures as a sample of type of cards I like…

Update: i have seen some enteries and i think it would look better if there is a big logo on one side and it has services under the big logo. And on the other side we can have contact details. However if you have different ideas I am open to suggestions

Will need high quality and editable files to print.

Name: Rashid
Mobile/WhatsApp: 07700900461
Email: Zan@quorvex-motors.example
Space to add snapchat and Instagram account if I decide to create one later.

Services to include in list ECU Remapping, Mileage correction, DPF issues, Retrofitting, Programming and Coding, Diagnostic Scans, Spare keys, Engine carbon Cleaning

```html
<!DOCTYPE html>
<html lang="en">
<head>
<meta charset="utf-8">
<title>Quorvex Tuning – Business Card</title>
<link rel="stylesheet" href="https://fonts.googleapis.com/css2?family=Open+Sans:wght@400;600;700&display=swap">
<style>
  :root {
    --backdrop: #e4e4e4;
    --card-dark: #050505;
    --card-light: #ffffff;
    --ink-light: #ffffff;
    --ink-dark: #111111;
    --accent-red: #d8121b;
    --swoosh: #000000;
  }
  * { margin: 0; padding: 0; box-sizing: border-box; }
  html, body {
    width: 1200px; height: 816px; overflow: hidden;
    background: var(--backdrop);
    font-family: "Open Sans", Arial, sans-serif;
  }
  .card {
    position: absolute;
    top: 261px;
    width: 464px; height: 299px;
    overflow: hidden;
  }
  .card--front { left: 67px; background: var(--card-dark); color: var(--ink-light); }
  .card--back { left: 641px; background: var(--card-light); color: var(--ink-dark); }

  .brand {
    position: absolute;
    display: flex; align-items: center; gap: 6px;
    font-weight: 700; letter-spacing: 0.04em;
    white-space: nowrap;
  }
  .brand__dot {
    width: 9px; height: 9px; border-radius: 50%;
    background: var(--accent-red);
  }
  .card--front .brand {
    left: 0; right: 0; top: 140px;
    justify-content: center;
    font-size: 19px; color: var(--ink-light);
  }
  .card--back .brand {
    left: 30px; top: 146px;
    font-size: 14px; color: var(--ink-dark);
  }

  .services {
    position: absolute; left: 0; right: 0; top: 227px;
    list-style: none;
    text-align: center;
    font-size: 12.5px; line-height: 20px;
  }
  .services li { display: inline; margin: 0 6px; }

  .name-tag {
    position: absolute; left: 231px; top: 33px;
    width: 193px; height: 52px;
    background: var(--accent-red); color: var(--ink-light);
    text-align: center;
  }
  .name-tag__name { display: block; font-size: 26px; line-height: 30px; padding-top: 2px; }
  .name-tag__role { display: block; font-size: 17px; line-height: 18px; }

  .contact {
    position: absolute; left: 200px; top: 96px;
    list-style: none;
    font-size: 20px; line-height: 27px;
    white-space: nowrap;
  }
  .contact--small { font-size: 14px; letter-spacing: -0.1px; }

  .swoosh {
    position: absolute; left: 0; top: 0;
    width: 464px; height: 299px;
  }
</style>
</head>
<body>
  <section class="card card--front" aria-label="Card front">
    <div class="brand"><span class="brand__dot"></span>QUORVEX TUNING</div>
    <ul class="services">
      <li>ECU Remapping</li><li>Mileage correction</li><li>DPF issues</li><li>Retrofitting</li><br>
      <li>Programming and Coding</li><li>Diagnostic Scans</li><li>Spare keys</li><br>
      <li>Engine carbon Cleaning</li>
    </ul>
  </section>

  <section class="card card--back" aria-label="Card back">
    <svg class="swoosh" viewBox="0 0 348 224" preserveAspectRatio="none" aria-hidden="true">
      <path fill="var(--swoosh)" d="M0,148 C30,195 110,222 150,214 C120,212 40,200 0,162 Z"/>
      <path fill="var(--swoosh)" d="M150,214 C200,206 240,172 286,158 C310,151 332,150 348,149 L348,160 C320,160 295,166 270,176 C230,192 195,214 150,214 Z"/>
    </svg>
    <div class="name-tag">
      <span class="name-tag__name">Rashid</span>
      <span class="name-tag__role">CEO</span>
    </div>
    <ul class="contact">
      <li>Tel. 07700900461</li>
      <li class="contact--small">Email: Zan@quorvex-motors.example</li>
      <li class="contact--small">www.quorvex-motors.example</li>
      <li>27 Mill Street N.Y</li>
    </ul>
    <div class="brand"><span class="brand__dot"></span>QUORVEX TUNING</div>
  </section>
</body>
</html>
```